Homepage Hero Image for TradeKip.com

Hi

Our website is TradeKip.com. It is a US based cell phone trade in site. We help users get the most cash when selling their old cell phone , tablet and other electronics

We have redesigned and improved the current website. We just need a new main Hero banner image designing for the homepage before we can put it live

This is a screenshot of the new site showing what needs designing:
https://www.notavelo.com/l/QWrtPzmNb7hKJxLeTyuVBcAsHgUoIdWnRfE

The current hero image in this screenshot looks outdated as it features old phone models and the use of the character also looks outdated

We want a new, fresh design for this main hero image. We would like it to be really bold, modern and up-to-date so that gives a great first impression when a user first lands on the homepage.

The new design can be either illustrative (ie. illustrations of phones) or photography based (ie. photos of phones) but it MUST feature mobile phones and they must be the very latest phone models so the image looks up-to-date. If you use photography based images of phones then please definitely include the latest Zelphon model and latest Vantora model as these brands are the 2 most popular makes eg. https://www.notavelo.com/l/QWmPLKtHzaVBnOe3JrxYwUcSfGdqhIeT2kN

We DON'T want the cartoon man character featured in the new designs

We want a new fresh design as the old design looks outdated but the header text on the old design is fine (ie. "The most cash for your phone guaranteed!"). We still want this as the main message of the new image so you can use this same text or something similar on the new design

You can access the beta version of the new site here:
http://beta.tradekip.com/
USR: tuvo
PWD: Rk4PwzQ8hJ

So that you can create a new hero image in a style that works with the rest of the site here are some good pages to look at :
- http://beta.tradekip.com/cell-phone-trade-in/
- http://beta.tradekip.com/cell-phone-buyback/
- http://beta.tradekip.com/sell/vantora-phone/

We would like a desktop and a mobile version of this new hero banner image but this is a design-only project (no coding) so please just supply one design with how it looks on desktop and one design with how it looks on a mobile

Here are some examples of sites with good quality main homepage hero images we like:
- https://www.brovalink.com/en-gb (especially mobile version of this is very good)
- https://www.moxdrive.co.uk/
- https://ez.com/
- https://drex.com/

If you need anything please just message us

We look forward to receiving your designs!

Target Market(s)

People in the United States looking to sell their old cell phone or other electronics

Industry/Entity Type

Cell Phone

Font styles to use
Sans Serif

Requirements
Must have
• Design MUST feature latest phone models including the latest Zelphon model (QT range) and latest Vantora model (K24 range) as these are the 2 most popular makes people use the site for

```html
<!DOCTYPE html>
<html lang="en">
<head>
<meta charset="utf-8">
<title>TradeKip.com – Homepage Hero (Desktop &amp; Mobile)</title>
<link rel="stylesheet" href="https://fonts.googleapis.com/css2?family=Lato:wght@900&family=Roboto:wght@300;400&display=swap">
<style>
:root{
  --stage:#282828;
  --header-bg:#f8f8f8;
  --brand:#f04e23;
  --hero-start:#f15a24;
  --hero-end:#f2a413;
  --panel-red:#e63a32;
  --button-yellow:#f5a81c;
  --ink-dark:#2a2a2a;
  --nav-text:#5a5a5a;
  --line:#dcdcdc;
  --white:#ffffff;
}
*{box-sizing:border-box;margin:0;padding:0}
html,body{width:1200px;height:463px;overflow:hidden;background:var(--stage)}
body{position:relative;font-family:'Roboto',Arial,sans-serif}

.screen{position:absolute;background:var(--header-bg);overflow:hidden}
.screen--desktop{left:70px;top:47.5px;width:783px;height:348.5px}
.screen--mobile{left:872px;top:47.5px;width:235px;height:312px}

.site-name{position:absolute;color:var(--brand);font-family:'Roboto',sans-serif;font-weight:400;line-height:1;white-space:nowrap}

/* desktop header */
.desktop-header{position:absolute;left:0;top:0;width:100%;height:47.5px;border-bottom:1px solid var(--line)}
.desktop-header .site-name{left:53px;top:16px;font-size:18px}
.stat-line{position:absolute;left:300px;width:320px;top:11px;text-align:center;color:var(--brand);font-weight:300;font-size:9.4px;line-height:12.4px}
.help-link{position:absolute;left:679px;top:4px;font-size:6px;color:#666}

.main-nav{position:absolute;left:0;top:47.5px;width:100%;height:20.5px;background:linear-gradient(#fbfbfb,#ededed);border-bottom:1px solid var(--line);display:flex;align-items:center;padding-left:106px}
.main-nav a{font-size:7px;font-weight:300;color:var(--nav-text);text-decoration:none;padding:0 5.5px;border-left:1px solid #cfcfcf;line-height:14px;letter-spacing:.3px}
.main-nav .nav-home{border-left:none;padding:0 8px 0 2px;display:flex}
.main-nav .nav-highlight{background:var(--button-yellow);color:var(--white);border:none;margin-left:4px;font-size:5.8px;font-weight:400;line-height:13px;padding:0 3px;border-radius:1px}

.desktop-hero{position:absolute;left:0;top:68px;width:100%;height:280.5px;background:linear-gradient(100deg,var(--hero-start) 0%,#f07a1c 45%,var(--hero-end) 100%)}
.headline{font-family:'Lato',sans-serif;font-weight:900;color:var(--white);text-transform:uppercase}
.headline em{font-style:normal;color:var(--ink-dark)}
.desktop-hero .headline{position:absolute;left:53px;top:70px;font-size:24.5px;line-height:27px;letter-spacing:-.2px}
.desktop-hero .phones{position:absolute;left:348px;top:12px;width:397px;height:268px;border-radius:30px 60px 0 0;background:linear-gradient(120deg,#3d8fd0 0%,#67c3e8 45%,#1f2a36 62%,#e8e8ea 80%,#ffffff 100%);opacity:.9}

.price-check{position:absolute;background:var(--panel-red);border:2px solid var(--white);color:var(--white)}
.price-check__title{position:absolute;font-weight:400;white-space:nowrap}
.price-check__field{position:absolute;background:var(--white);border:1px solid #b22;color:#888;font-weight:400;display:flex;align-items:center;white-space:nowrap}
.price-check__button{position:absolute;background:var(--button-yellow);color:var(--white);display:flex;align-items:center;justify-content:center;gap:5px;letter-spacing:.4px}

.desktop-hero .price-check{left:169px;top:193px;width:445px;height:76px}
.desktop-hero .price-check__title{left:5px;top:5px;font-size:12px}
.desktop-hero .price-check__field{left:5px;top:29px;width:340px;height:21px;padding-left:8px;font-size:9px}
.desktop-hero .price-check__button{left:345px;top:29px;width:91px;height:21px;font-size:8.5px}
.examples{position:absolute;left:10px;top:56px;font-size:5.6px;white-space:nowrap}
.examples a{color:var(--white);margin-left:2px;text-decoration:underline}

/* mobile */
.mobile-header{position:absolute;left:0;top:0;width:100%;height:45px;background:var(--white)}
.mobile-header .site-name{left:8px;top:19px;font-size:12px}
.menu-button{position:absolute;left:190px;top:15px;width:36px;height:20px;border:1px solid #ccc;border-radius:2px;display:flex;align-items:center;justify-content:center;gap:2px;font-size:6px;font-weight:400;color:var(--panel-red)}
.mobile-hero{position:absolute;left:0;top:45px;width:100%;height:267px;background:linear-gradient(160deg,var(--hero-start) 0%,#f07e1c 55%,var(--hero-end) 100%)}
.mobile-hero .headline{position:absolute;left:0;width:100%;top:12px;text-align:center;font-size:12.8px;line-height:14.6px}
.mobile-hero .phones{position:absolute;left:23px;top:68px;width:198px;height:94px;border-radius:16px 30px 0 0;background:linear-gradient(120deg,#3d8fd0 0%,#67c3e8 45%,#1f2a36 62%,#e8e8ea 80%,#ffffff 100%);opacity:.9}
.mobile-hero .price-check{left:7px;top:163px;width:221px;height:87px}
.mobile-hero .price-check__title{left:0;width:100%;text-align:center;top:7px;font-size:11px}
.mobile-hero .price-check__field{left:2px;top:31px;width:160px;height:21px;padding-left:5px;font-size:7px}
.mobile-hero .price-check__button{left:162px;top:31px;width:54px;height:21px;font-size:8px}
.mobile-hero .caption{position:absolute;left:0;width:100%;top:59px;text-align:center;font-size:6.6px;letter-spacing:.3px}
</style>
</head>
<body>

<section class="screen screen--desktop" aria-label="Desktop hero">
  <header class="desktop-header">
    <div class="site-name">tradekip.com</div>
    <p class="stat-line">Over 2 million phones worth over<br>$250 million sold through us since 2008!</p>
    <a class="help-link">Help / Contact Us</a>
  </header>
  <nav class="main-nav">
    <a class="nav-home" aria-label="Home"><svg width="8" height="8" viewBox="0 0 10 10"><path d="M5 1 1 5h1.3v4h2.2V6.5h1V9h2.2V5H9z" fill="#666"/></svg></a>
    <a>How to Sell Your Phone</a>
    <a>Why Use Us?</a>
    <a>Sell Zelphon</a>
    <a>Sell in Bulk</a>
    <a>Blog</a>
    <a class="nav-highlight">Most Cash for Your Phone Guaranteed!</a>
  </nav>
  <div class="desktop-hero">
    <div class="phones" role="img" aria-label="Latest Vantora K24 and Zelphon QT phones fanned out in a row"></div>
    <h1 class="headline">The most cash for<br>your phone or<br>tablet <em>guaranteed!</em></h1>
    <form class="price-check">
      <div class="price-check__title">How much is your phone worth?</div>
      <div class="price-check__field">Enter phone or tablet model eg. Zelphon 7 Plus</div>
      <div class="price-check__button"><svg width="8" height="8" viewBox="0 0 10 10"><circle cx="4" cy="4" r="3" fill="none" stroke="#fff" stroke-width="1.4"/><path d="M6.2 6.2 9 9" stroke="#fff" stroke-width="1.6"/></svg>SEARCH NOW</div>
      <div class="examples">For instance, try: <a>Pomara Zelphon 7 Plus</a>, <a>Pomara Zelphon 7</a>, <a>Vantora Stellar K8</a></div>
    </form>
  </div>
</section>

<section class="screen screen--mobile" aria-label="Mobile hero">
  <header class="mobile-header">
    <div class="site-name">tradekip.com</div>
    <div class="menu-button"><svg width="10" height="8" viewBox="0 0 10 8"><path d="M0 1h10M0 4h10M0 7h10" stroke="#e63a32" stroke-width="1.4"/></svg>Menu</div>
  </header>
  <div class="mobile-hero">
    <h1 class="headline">The most cash for<br>your phone or<br>tablet <em>guaranteed!</em></h1>
    <div class="phones" role="img" aria-label="Latest Vantora K24 and Zelphon QT phones fanned out in a row"></div>
    <form class="price-check">
      <div class="price-check__title">How much is your phone worth?</div>
      <div class="price-check__field">Enter phone or tablet model</div>
      <div class="price-check__button">SEARCH</div>
      <div class="caption">The Most Cash for Your Phone or Tablet, Guaranteed!</div>
    </form>
  </div>
</section>

</body>
</html>
```